"Drink Champagne and Dance on the Table" sort of business card needed!

We throw events, weddings, engagement parties, baby showers and the sort of end of year corporate events that people remember long after the glitter has settled - the sort of events that make you stand still and say wow when you walk in and then make you want to "Drink Champagne and Dance on the Tables"

We have a great logo with heaps of potential and need a business card that just screams creative professionals!

We are based in Auckland, NZ and are priced at the Premium end of the market were there are around 10 other main competitors. We need to stand out and make a strong statement about who we are!

Our Business Card will be one of the few items that we print out so are fully prepared to invest in a premium print job.

We really love our logo and think it has heaps of potential! Its ok if you would like to manipulate it (maybe put it on an angle, or use the circle element on its own?).

Black and Gold is very striking, but its very done in our market so we would like to avoid a solid black background please

We have done a bit of an inspiration document to give you an idea of the sort of look and feel we are hoping to achieve.

Target Market(s)

Woman aged 30 - 45 with an income bracket of $70k +

Industry/Entity Type

Event Planning

Contact Information for Business Card

Marnie
hello@fennoriwick.co.nz
www.fennoriwick.co.nz
02734419027

Number of Pages Required

5+ page

Requirements
Must have
• Vibrant colours and design (we love the vibrant pink and gold in the inspiration file)
• We would love to see some colour and creativity (although the black and gold is very striking). Because we are doing such minimal print work I am happy for the cards to be a little more expensive so if you want to use cut outs, rounded corners, gold foil, non standard size etc I am happy for that too. I really want the wow factor.
Nice to have
• We would like the design to be double sided.
Should not have
• The logo colour changed
• Use of Purple or Green or solid black background.
• Wedding Photos!

```html
<!DOCTYPE html>
<html lang="en">
<head>
<meta charset="utf-8">
<title>Fenno and Riwick – Business Cards</title>
<link rel="stylesheet" href="https://fonts.googleapis.com/css2?family=Raleway:wght@300;400;600&display=swap">
<style>
  :root {
    --backdrop: #2a2e35;
    --pink: #d8457c;
    --pink-deep: #9e2553;
    --pink-ink: #fff4f7;
    --rose: #b3325f;
    --rose-deep: #7c1c40;
    --gold: #ecc872;
    --card-w: 540px;
    --card-h: 310px;
  }
  * { box-sizing: border-box; margin: 0; padding: 0; }
  html, body {
    width: 1200px; height: 848px; overflow: hidden;
    background: var(--backdrop);
    font-family: "Raleway", sans-serif;
  }
  .card-set {
    position: absolute; inset: 0;
    display: flex; align-items: center; justify-content: center; gap: 40px;
  }
  .card {
    position: relative;
    width: var(--card-w); height: var(--card-h);
    border-radius: 30px;
    box-shadow: 0 18px 40px rgba(0,0,0,.45);
    overflow: hidden;
  }
  .card--front { background: var(--pink); color: var(--pink-ink); --ring: var(--pink-deep); --ink: var(--pink-ink); }
  .card--back  { background: var(--rose); color: var(--gold); --ring: var(--rose-deep); --ink: var(--gold); }

  .seal {
    position: absolute; left: 45px; top: 60px;
    width: 190px; height: 190px; border-radius: 50%;
    border: 6px solid var(--ring);
    display: flex; align-items: center; justify-content: center; text-align: center;
  }
  .seal__name {
    font-weight: 600; font-size: 19px; line-height: 1.25; letter-spacing: .02em;
    color: var(--ring); width: 120px;
  }

  .details {
    position: absolute; left: 280px; top: 26px; width: 230px;
    display: flex; flex-direction: column;
  }
  .brand { display: flex; flex-direction: column; align-items: center; }
  .brand__ring {
    width: 64px; height: 64px; border-radius: 50%;
    border: 2px solid var(--ink); margin-bottom: 10px;
  }
  .brand__name { font-weight: 600; font-size: 22px; letter-spacing: .01em; white-space: nowrap; }
  .brand__tag { font-size: 8px; letter-spacing: .35em; margin-top: 4px; font-weight: 400; }
  .person { font-weight: 300; font-size: 24px; letter-spacing: .08em; margin: 20px 0 10px; }
  .contact-list { list-style: none; }
  .contact-list li {
    display: flex; align-items: center; gap: 10px;
    font-size: 14px; font-weight: 400; margin-bottom: 8px; letter-spacing: .02em;
    white-space: nowrap;
  }
  .contact-list svg { width: 14px; height: 14px; flex: none; }
</style>
</head>
<body>
<main class="card-set">

  <section class="card card--front" aria-label="Card front">
    <div class="seal"><span class="seal__name">Fenno and Riwick</span></div>
    <div class="details">
      <div class="brand">
        <span class="brand__ring"></span>
        <span class="brand__name">Fenno and Riwick</span>
        <span class="brand__tag">WEDDINGS &amp; EVENTS</span>
      </div>
      <p class="person">Marnie</p>
      <ul class="contact-list">
        <li><svg viewBox="0 0 14 14" fill="none" stroke="currentColor" stroke-width="1.3"><rect x="1" y="3" width="12" height="8"/><path d="M1 3l6 5 6-5"/></svg>hello@fennoriwick.co.nz</li>
        <li><svg viewBox="0 0 14 14" fill="none" stroke="currentColor" stroke-width="1.2"><circle cx="7" cy="7" r="6"/><ellipse cx="7" cy="7" rx="2.6" ry="6"/><path d="M1 7h12"/></svg>www.fennoriwick.co.nz</li>
        <li><svg viewBox="0 0 14 14" fill="none" stroke="currentColor" stroke-width="1.3"><rect x="1" y="2" width="12" height="10" rx="2"/><circle cx="7" cy="8" r="2.3"/><path d="M3 5h8"/></svg>02734419027</li>
      </ul>
    </div>
  </section>

  <section class="card card--back" aria-label="Card back">
    <div class="seal"><span class="seal__name">Fenno and Riwick</span></div>
    <div class="details">
      <div class="brand">
        <span class="brand__ring"></span>
        <span class="brand__name">Fenno and Riwick</span>
        <span class="brand__tag">WEDDINGS &amp; EVENTS</span>
      </div>
      <p class="person">Marnie</p>
      <ul class="contact-list">
        <li><svg viewBox="0 0 14 14" fill="none" stroke="currentColor" stroke-width="1.3"><rect x="1" y="3" width="12" height="8"/><path d="M1 3l6 5 6-5"/></svg>hello@fennoriwick.co.nz</li>
        <li><svg viewBox="0 0 14 14" fill="none" stroke="currentColor" stroke-width="1.2"><circle cx="7" cy="7" r="6"/><ellipse cx="7" cy="7" rx="2.6" ry="6"/><path d="M1 7h12"/></svg>www.fennoriwick.co.nz</li>
        <li><svg viewBox="0 0 14 14" fill="none" stroke="currentColor" stroke-width="1.3"><rect x="1" y="2" width="12" height="10" rx="2"/><circle cx="7" cy="8" r="2.3"/><path d="M3 5h8"/></svg>02734419027</li>
      </ul>
    </div>
  </section>

</main>
</body>
</html>
```